Etiketten-Design für Honiggläser
Zielgruppe
kleine Hobby-Imkerei, Zielgruppe 'Regionale Käufer', die gerne Wissen, wo ihr Honig her kommt. Mittleres Preissegment
Aufgabenstellung
Das Etikett soll für meine Honiggläser dienen. Die Maße sind 134 x 64 mm. Die Breite kann bis 150 mm variieren, die Höhe nicht.
Pflichtangaben : 'Deutscher xxx Honig (z.B. Blütenhonig), Name und Anschrift (Jonas Welke Birkenweg 12 73512 Ludwigsburg J.Welke@postfeld.de), mindestens haltbar bis(wird gestempelt, Fläche min. 30x7mm, Gewicht 500 g(Schriftgröße min. 4 mm), 'Mehrwegglas'. Schriftgröße mindestens 1,2mm bezogen auf das kleine „x“. Optional Lagerbedingungen, s. bisheriges Etikett.
Das angehängte Bild soll in irgendeiner Form mit eingebunden wäre, gerne können Farben und Form aber verändert werden, Bildrechte sind bei mir. Anbei auch mein bisheriges, selber entworfenes Etikett.
Das neue Etikett soll moderner und ansprechender werden, der Regionalitätsbezug etwas besser herausgearbeitet werden. Gelb hat sich als Farbe nicht bewährt, da das gelb des Honig sich manchmal beißt.

```html
<!DOCTYPE html>
<html lang="de">
<head>
<meta charset="utf-8">
<title>Honigetikett Frühtracht</title>
<link rel="stylesheet" href="https://fonts.googleapis.com/css2?family=Patrick+Hand&family=Barlow:wght@400;500&display=swap">
<style>
  :root {
    --page: #fafafa;
    --frame: #555555;
    --ink: #111111;
    --label-bg: #ffffff;
    --spring-green: #8cc21c;
    --meadow: #2fae2a;
    --meadow-deep: #1f7d1c;
    --field: #d8c23a;
    --sky: #6aa9df;
    --title-white: #ffffff;
    --title-shadow: rgba(120, 70, 20, 0.55);
  }
  * { box-sizing: border-box; margin: 0; padding: 0; }
  html, body { width: 1200px; height: 1200px; overflow: hidden; }
  body {
    background: var(--page);
    border: 1px solid var(--frame);
    position: relative;
    font-family: "Barlow", sans-serif;
    color: var(--ink);
  }
  .label {
    position: absolute;
    left: 184px; top: 407px;
    width: 845px; height: 403px;
    border: 1px solid var(--ink);
    background: var(--label-bg);
    overflow: hidden;
  }
  .label__scene {
    position: absolute;
    left: 0; top: 0;
    width: 556px; height: 100%;
    background: linear-gradient(180deg, var(--sky) 0%, #7fb35a 16%, var(--field) 30%, #9cc63a 40%, var(--meadow) 55%, var(--meadow-deep) 100%);
  }
  .scene-title {
    position: absolute;
    left: 0; width: 556px;
    text-align: center;
    font-family: "Patrick Hand", cursive;
    color: var(--title-white);
    text-shadow: 2px 3px 0 var(--title-shadow);
    line-height: 1;
  }
  .scene-title--main { top: 58px; font-size: 72px; letter-spacing: 1px; }
  .scene-title--main span { display: block; margin-bottom: 2px; }
  .scene-title--origin { top: 331px; font-size: 29px; text-shadow: 1px 2px 0 var(--title-shadow); }

  .label__info {
    position: absolute;
    left: 556px; top: 0;
    width: 288px; height: 100%;
    border-left: 1px solid var(--ink);
  }
  .info-line { position: absolute; left: 0; width: 100%; text-align: center; line-height: 1; }
  .product-name { top: 20px; font-family: "Patrick Hand", cursive; font-size: 33px; }
  .product-variety { top: 52px; font-family: "Patrick Hand", cursive; font-size: 31px; color: var(--spring-green); }
  .rule { position: absolute; height: 1px; background: var(--ink); }
  .rule--top { left: 20px; width: 251px; top: 91px; }
  .rule--date { left: 16px; width: 255px; top: 329px; }
  .own-apiary { top: 103px; font-family: "Patrick Hand", cursive; font-size: 21px; letter-spacing: 0.5px; }
  .address { top: 146px; font-size: 16px; line-height: 20px; }
  .storage {
    position: absolute; left: 16px; top: 228px;
    font-size: 11.5px; line-height: 16px;
  }
  .storage strong { font-weight: 500; }
  .best-before { position: absolute; left: 16px; top: 312px; font-size: 12.5px; font-weight: 500; }
  .returnable { position: absolute; left: 16px; top: 337px; font-size: 9.5px; letter-spacing: 0.6px; }
  .weight { position: absolute; right: 16px; top: 352px; font-size: 25px; }
</style>
</head>
<body>
  <main class="label">
    <section class="label__scene" role="img" aria-label="Gemalte Frühlingswiese mit blühenden Obstbäumen und vier weißen Bienenbeuten">
      <h1 class="scene-title scene-title--main"><span>DEUTSCHER</span><span>HONIG</span></h1>
      <p class="scene-title scene-title--origin">AUS LUDWIGSBURG</p>
    </section>
    <section class="label__info">
      <p class="info-line product-name">DEUTSCHER HONIG</p>
      <p class="info-line product-variety">FRÜHTRACHT</p>
      <div class="rule rule--top"></div>
      <p class="info-line own-apiary">— AUS EIGENER IMKEREI —</p>
      <address class="info-line address" style="font-style: normal;">
        Jonas Welke,<br>
        Birkenweg 12, 73512 Ludwigsburg,<br>
        J.Welke@postfeld.de
      </address>
      <p class="storage">
        <strong>Trocken, kühl und dunkel lagern</strong><br>
        Honig kann fest werden, Sie können kristallisierten<br>
        Honig im Wassebad (bis 40°) wieder verflüssigen
      </p>
      <p class="best-before">mindestens haltbar bis:</p>
      <div class="rule rule--date"></div>
      <p class="returnable">MEHRWEGGLAS</p>
      <p class="weight">500 g</p>
    </section>
  </main>
</body>
</html>
```